Business Card Design

Need a hot business card in wine colors something cool and mod please feel free to be , FUNKY and free with this .
Updates

Industry/Entity Type

Business

Contact Information for Business Card

KALIMERO HAIR DESIGN 2918 w 3rd st scottsdale az 85019 Custom modern hair design and custom color by MARCUS DOVELING 602-4813926 cell salon 480 -317-2064 email marcusdoveling@plumbox.net hours wed thru sat 7am to 6pm.

Font styles to use
Other font styles liked:
• something fun and mod.

Colors
a54599
6b449b
1b1b1b
606060

Requirements
Must have
• Apointment reminder on flip side of card.
Should not have
• Nothing boring.

```html
<!DOCTYPE html>
<html lang="en">
<head>
<meta charset="utf-8">
<title>Kalimero Hair Design – Business Card</title>
<link href="https://fonts.googleapis.com/css2?family=Open+Sans:wght@400;600&family=Allura&display=swap" rel="stylesheet">
<style>
  :root {
    --stage: #e9e4ea;
    --orchid: #c15fc3;
    --orchid-light: #d57bd6;
    --wine: #a54599;
    --violet: #6b449b;
    --violet-light: #8157b0;
    --white: #ffffff;
    --white-soft: rgba(255,255,255,0.85);
    --ink: #1b1b1b;
  }
  * { box-sizing: border-box; margin: 0; padding: 0; }
  html, body {
    width: 1200px; height: 1023px; overflow: hidden;
    background: var(--stage);
    font-family: "Open Sans", Arial, sans-serif;
    color: var(--white);
  }
  .stage { position: relative; width: 1200px; height: 1023px; }

  .card {
    position: absolute; width: 760px; height: 434px;
    border-radius: 22px; overflow: hidden;
    box-shadow: 0 10px 30px rgba(27,27,27,0.25);
  }
  .card-back { left: 80px; top: 56px; }
  .card-front { left: 360px; top: 533px; }
  .card-art { position: absolute; inset: 0; width: 100%; height: 100%; }

  .brand { position: absolute; display: flex; align-items: center; gap: 14px; }
  .brand-mark {
    width: 74px; height: 74px; border-radius: 6px;
    background: var(--violet);
  }
  .brand-name {
    font-weight: 400; font-size: 30px; line-height: 1.05;
    letter-spacing: 1px; color: var(--white);
  }

  /* back: appointment reminder */
  .card-back .brand { left: 34px; top: 40px; }
  .divider-v {
    position: absolute; left: 378px; top: 38px; width: 1px; height: 82px;
    background: var(--white-soft);
  }
  .reminder-title {
    position: absolute; left: 402px; top: 48px;
    font-family: "Allura", cursive; font-size: 40px; color: var(--white);
  }
  .hours { position: absolute; left: 0; right: 0; top: 136px; text-align: center; font-size: 15px; }
  .hours-label { font-weight: 600; }
  .hours-line { letter-spacing: 0.3px; }
  .slots { position: absolute; left: 44px; right: 44px; top: 236px; }
  .slot-row { display: flex; gap: 30px; height: 46px; align-items: flex-end; font-size: 18px; }
  .slot { display: flex; align-items: flex-end; gap: 8px; }
  .slot-date { flex: 1.5; }
  .slot-time { flex: 1; }
  .slot-line { flex: 1; border-bottom: 1px dotted var(--white-soft); margin-bottom: 5px; }

  /* front: contact card */
  .card-front .brand { left: 44px; top: 52px; }
  .person { position: absolute; right: 80px; top: 156px; text-align: right; }
  .person-name { font-size: 22px; }
  .person-title { font-size: 14px; color: var(--white-soft); }
  .rule {
    position: absolute; left: 48px; top: 200px; width: 510px; height: 1px;
    background: linear-gradient(90deg, rgba(255,255,255,0.2), rgba(255,255,255,0.8));
  }
  .contact-list { position: absolute; left: 50px; top: 222px; list-style: none; font-size: 17px; }
  .contact-list li { display: flex; align-items: center; gap: 10px; height: 22px; }
  .contact-list svg { width: 13px; height: 13px; fill: var(--white); flex: none; }
  .tagline {
    position: absolute; left: 0; right: 0; bottom: 16px;
    text-align: center; font-size: 19px; color: var(--white);
  }
</style>
</head>
<body>
<main class="stage">

  <section class="card card-back" aria-label="Appointment reminder side">
    <svg class="card-art" viewBox="0 0 760 434" preserveAspectRatio="none">
      <defs>
        <linearGradient id="back-top" x1="0" y1="0" x2="1" y2="1">
          <stop offset="0" stop-color="#b553b8"/>
          <stop offset="1" stop-color="#cf70cf"/>
        </linearGradient>
        <linearGradient id="back-band" x1="0" y1="0" x2="1" y2="0">
          <stop offset="0" stop-color="#7049a3"/>
          <stop offset="0.55" stop-color="#8a5cb6"/>
          <stop offset="1" stop-color="#6b449b"/>
        </linearGradient>
        <radialGradient id="back-portrait" cx="0.5" cy="0.5" r="0.5">
          <stop offset="0" stop-color="#e39ae2" stop-opacity="0.55"/>
          <stop offset="1" stop-color="#e39ae2" stop-opacity="0"/>
        </radialGradient>
      </defs>
      <rect width="760" height="434" fill="url(#back-top)"/>
      <rect x="420" y="10" width="300" height="190" fill="url(#back-portrait)" role="img" aria-label="Faint portrait of a model with styled hair"/>
      <path d="M0 196 Q380 150 760 170 L760 434 L0 434 Z" fill="#9a4fb0" opacity="0.6"/>
      <path d="M0 208 Q380 168 760 186 L760 434 L0 434 Z" fill="url(#back-band)"/>
    </svg>
    <div class="brand">
      <div class="brand-mark"></div>
      <div class="brand-name">KALIMERO<br>HAIR DESIGN</div>
    </div>
    <div class="divider-v"></div>
    <div class="reminder-title">Your Next Appointment</div>
    <div class="hours">
      <div class="hours-label">Openning Hours:</div>
      <div class="hours-line">Wednesday to Saturday ........ 7:00am to 6:00pm</div>
    </div>
    <div class="slots">
      <div class="slot-row"><div class="slot slot-date">Date:<span class="slot-line"></span></div><div class="slot slot-time">Time:<span class="slot-line"></span></div></div>
      <div class="slot-row"><div class="slot slot-date">Date:<span class="slot-line"></span></div><div class="slot slot-time">Time:<span class="slot-line"></span></div></div>
      <div class="slot-row"><div class="slot slot-date">Date:<span class="slot-line"></span></div><div class="slot slot-time">Time:<span class="slot-line"></span></div></div>
      <div class="slot-row"><div class="slot slot-date">Date:<span class="slot-line"></span></div><div class="slot slot-time">Time:<span class="slot-line"></span></div></div>
    </div>
  </section>

  <section class="card card-front" aria-label="Contact side">
    <svg class="card-art" viewBox="0 0 760 434" preserveAspectRatio="none">
      <defs>
        <linearGradient id="front-bg" x1="0" y1="0" x2="1" y2="1">
          <stop offset="0" stop-color="#b455b9"/>
          <stop offset="0.5" stop-color="#cd6bcc"/>
          <stop offset="1" stop-color="#b452b6"/>
        </linearGradient>
        <linearGradient id="front-band" x1="0" y1="0" x2="1" y2="0">
          <stop offset="0" stop-color="#7a4aa8"/>
          <stop offset="0.5" stop-color="#8b5cb8"/>
          <stop offset="1" stop-color="#6b449b"/>
        </linearGradient>
        <radialGradient id="front-portrait" cx="0.5" cy="0.5" r="0.5">
          <stop offset="0" stop-color="#e6a2e4" stop-opacity="0.5"/>
          <stop offset="1" stop-color="#e6a2e4" stop-opacity="0"/>
        </radialGradient>
      </defs>
      <rect width="760" height="434" fill="url(#front-bg)"/>
      <rect x="440" y="40" width="320" height="300" fill="url(#front-portrait)" role="img" aria-label="Faint portrait of a model with styled hair"/>
      <path d="M0 348 Q380 322 760 330 L760 434 L0 434 Z" fill="#a052b4" opacity="0.6"/>
      <path d="M0 360 Q380 336 760 346 L760 434 L0 434 Z" fill="url(#front-band)"/>
    </svg>
    <div class="brand">
      <div class="brand-mark"></div>
      <div class="brand-name">KALIMERO<br>HAIR DESIGN</div>
    </div>
    <div class="person">
      <div class="person-name">Marcus Doveling</div>
      <div class="person-title">Designated Title</div>
    </div>
    <div class="rule"></div>
    <ul class="contact-list">
      <li><svg viewBox="0 0 16 16" aria-hidden="true"><path d="M4 0h8a1 1 0 0 1 1 1v14a1 1 0 0 1-1 1H4a1 1 0 0 1-1-1V1a1 1 0 0 1 1-1zm1 2v10h6V2zm3 11a1 1 0 1 0 0 2 1 1 0 0 0 0-2z"/></svg>602-481-3926</li>
      <li><svg viewBox="0 0 16 16" aria-hidden="true"><path d="M1 5c2-3 12-3 14 0l-1 2-3-1V5H5v1L2 7zM3 9h10l1 6H2zm5 1.5a2 2 0 1 0 0 4 2 2 0 0 0 0-4z"/></svg>480-317-2064</li>
      <li><svg viewBox="0 0 16 16" aria-hidden="true"><path d="M0 3h16v10H0zm1.5 1.5L8 9l6.5-4.5V4h-13z"/></svg>marcusdoveling@plumbox.net</li>
      <li><svg viewBox="0 0 16 16" aria-hidden="true"><path d="M8 0a5.5 5.5 0 0 1 5.5 5.5C13.5 10 8 16 8 16S2.5 10 2.5 5.5A5.5 5.5 0 0 1 8 0zm0 3.5a2 2 0 1 0 0 4 2 2 0 0 0 0-4z"/></svg>2918 W 3rd St Scottsdale, AZ 85019</li>
    </ul>
    <div class="tagline">Custom Modern Hair Design and Custom Color</div>
  </section>

</main>
</body>
</html>
```